Industry Leading Audio Visual Company needs a new sales brochure (Leave behind)

We are developing a bi-fold brochure that our sales team can either send to or leave with potential new customers. Brandt-Hollis are an Audio Visual Integrator, we design and build any facilities requiring sound or vision. Boardrooms, lecture theaters, classrooms etc. Visit our website at www.brandt-hollis-example.com for more info.
We are well respected in North and South Carolina and have been in business since 1983. We are looking for a brochure that represents our company, focusing on how we look after our customers, rather than just advertising what products we sell. The comments below are from our sales team where they tell us what they want the brochure to convey.
Using a similar theme to the website would be good to maintain our corporate look, and feel free to use any photos from our website in your proposal.

Target Market(s)

Corporate / Government / Higher Education / Houses of Worship

Industry/Entity Type

Technology Equipment

Font styles to use
Serif
Sans Serif

Colors
3176b5
cedeed
85cae6

Requirements
Must have
• Emphasize our experience and that we have huge client retention.

```html
<!DOCTYPE html>
<html lang="en">
<head>
<meta charset="utf-8">
<title>Visual Impact – Brochure Page 03</title>
<link href="https://fonts.googleapis.com/css2?family=Open+Sans:wght@300;400;600&display=swap" rel="stylesheet">
<style>
  :root {
    --brand-blue: #1d5f93;
    --heading-blue: #2a6ea8;
    --text-dark: #2b2b2b;
    --text-light: #ffffff;
    --page-bg: #f4f4f4;
    --paper: #ffffff;
  }
  * { margin: 0; padding: 0; box-sizing: border-box; }
  html, body { width: 939px; height: 1200px; overflow: hidden; background: var(--paper); }
  body { font-family: "Open Sans", sans-serif; color: var(--text-dark); position: relative; }

  .page-sheet {
    position: absolute; left: 26px; top: 14px; width: 564px; height: 1170px;
    background: linear-gradient(90deg, #f1f1f1 0%, #ffffff 14%, #ffffff 100%);
  }
  .feature-panel {
    position: absolute; left: 590px; top: 14px; width: 349px; height: 1170px;
    background: var(--brand-blue); color: var(--text-light);
  }

  .room-block { position: absolute; left: 66px; width: 276px; }
  .room-title { font-size: 18px; font-weight: 600; color: var(--heading-blue); line-height: 1.2; margin-bottom: 12px; }
  .room-text { font-size: 12.4px; line-height: 19px; font-weight: 400; }

  .photo { position: absolute; }
  .photo-room { left: 343px; width: 231px; }

  .panel-title { position: absolute; left: 25px; top: 42px; font-size: 39px; font-weight: 300; letter-spacing: 0.5px; line-height: 1; }
  .panel-subtitle { position: absolute; left: 25px; top: 108px; width: 300px; font-size: 18.5px; font-weight: 300; line-height: 26.5px; }
  .service { position: absolute; left: 25px; width: 300px; }
  .service-title { font-size: 17.5px; font-weight: 600; margin-bottom: 12px; line-height: 1.2; }
  .service-text { font-size: 12.3px; line-height: 19px; text-align: justify; font-weight: 400; }
  .service-photo { position: absolute; left: 29px; width: 270px; }
  .page-number { position: absolute; right: 26px; top: 1118px; font-size: 19px; font-weight: 400; }
</style>
</head>
<body>
  <div class="page-sheet"></div>

  <section class="room-block" style="top:52px">
    <h2 class="room-title">Conference Rooms</h2>
    <p class="room-text">Well equipped, easy to use and comfortable conference rooms are crucial to the productivity of your teams. Control systems must be designed for intuitive use.</p>
  </section>
  <div class="photo photo-room" style="top:60px;height:154px;background:linear-gradient(180deg,#b8a98e 0%,#6f6655 55%,#8d8a80 100%)" role="img" aria-label="Conference room with long table, chairs and two wall displays"></div>

  <section class="room-block" style="top:212px">
    <h2 class="room-title">Video Conference Rooms</h2>
    <p class="room-text">Video conference rooms are very special spaces with a singular purpose; to bring people together from two or more remote locations in the most engaging way possible.</p>
  </section>
  <div class="photo photo-room" style="top:229px;height:142px;background:linear-gradient(180deg,#cdb27a 0%,#7d6a4a 55%,#d8cfae 100%)" role="img" aria-label="Video conference room with curved table facing a wall of screens"></div>

  <section class="room-block" style="top:368px">
    <h2 class="room-title">Boardrooms</h2>
    <p class="room-text">The boardroom is not only the statement room for your company, but it should also be a secure, efficient, comfortable and easy to use meeting space for your executives.</p>
  </section>
  <div class="photo photo-room" style="top:386px;height:139px;background:linear-gradient(180deg,#8a6d52 0%,#5a3c28 55%,#6e5a4a 100%)" role="img" aria-label="Wood-panelled boardroom with long table and leather chairs"></div>

  <section class="room-block" style="top:516px">
    <h2 class="room-title">Auditoriums</h2>
    <p class="room-text" style="width:280px">Large event spaces such as auditoriums require high-end professional sound and video distribution.&nbsp; Of course, a complete assessment of the native acoustic characteristics of the space are critical to properly designing a system that will enhance performance and audience enjoyment.</p>
  </section>
  <div class="photo photo-room" style="top:540px;height:146px;background:linear-gradient(180deg,#c9c2b6 0%,#2c3f8a 30%,#2a3678 62%,#a8352a 100%)" role="img" aria-label="Auditorium with large video wall above red seating"></div>

  <section class="room-block" style="top:701px">
    <h2 class="room-title">Divisible Rooms</h2>
    <p class="room-text">Meeting spaces that can be combined or divided provide a great deal of flexibility but this feature also has its challenges when it comes to distributing audio and visual content among the spaces.</p>
  </section>
  <div class="photo photo-room" style="top:704px;height:146px;background:linear-gradient(180deg,#dcd9d2 0%,#b8b3a8 45%,#8a7454 100%)" role="img" aria-label="Divisible meeting room with U-shaped tables and projection screens"></div>

  <div class="photo" style="left:67px;top:881px;width:514px;height:237px;background:linear-gradient(180deg,#d8d2c6 0%,#bcb3a2 38%,#9a8466 62%,#3b3634 100%)" role="img" aria-label="Tiered lecture room with curved desks, chairs and three projection screens"></div>

  <aside class="feature-panel">
    <h1 class="panel-title">VISUAL IMPACT</h1>
    <p class="panel-subtitle">Creating a Statement and Reinforcing Your Brand Through Audio Visual Excellence</p>

    <section class="service" style="top:226px">
      <h2 class="service-title">Video Walls</h2>
      <p class="service-text">Video walls capture interest with a “wow” factor that only high-end corporations could traditionally afford, but this is no longer true.</p>
    </section>
    <div class="service-photo" style="top:326px;height:146px;background:linear-gradient(90deg,#e2612a 0%,#3a4c7a 30%,#e86a2c 55%,#f3f0ea 70%,#e06430 100%)" role="img" aria-label="Innovation centre lobby with large orange-framed video wall"></div>

    <section class="service" style="top:489px">
      <h2 class="service-title">Digital Signage</h2>
      <p class="service-text">Video walls capture interest with a “wow” factor that only high-end corporations could traditionally afford, but this is no longer true.</p>
    </section>
    <div class="service-photo" style="top:593px;height:170px;background:linear-gradient(90deg,#e8e4dc 0%,#c9b69a 30%,#2d7a3a 60%,#3f8d4a 85%,#8a5a30 100%)" role="img" aria-label="Digital signage display set into a wooden wall showing event information"></div>

    <section class="service" style="top:779px">
      <h2 class="service-title">Wayfinding Solutions</h2>
      <p class="service-text">Large organizations such as hospitals, universities and shopping centers are difficult to navigate but digital wayfinding solutions provide the answer to getting visitors where they need to go quickly and efficiently.</p>
    </section>
    <div class="service-photo" style="top:922px;height:170px;background:linear-gradient(135deg,#7a3a4a 0%,#d9c8c0 45%,#e8ded6 65%,#6aa8b8 100%)" role="img" aria-label="Visitor using an interactive touchscreen wayfinding kiosk"></div>

    <div class="page-number">03</div>
  </aside>
</body>
</html>
```